Transformative School Model Needs a Website. I am easy to work with.

Greetings:
I am creating a K-12 school that is a complete and total re-imagination of what education can be for children, families, communities, and the planet. While we will begin as a K-12 school, I really see it as a complete life cycle education (birth to death). I'm looking for a website to describe my new transformational educational model. I anticipate having 7-8 pages. I have all the copy ready.
I am the Founder. I am easy to work with, an effective communicator, and I’m very good at knowing what I want and providing specific and concrete detail, examples, and direction to make sure I use your time wisely.

```html
<!DOCTYPE html>
<html lang="en">
<head>
<meta charset="utf-8">
<title>Serene Accord Academy</title>
<link href="https://fonts.googleapis.com/css2?family=Playfair+Display:ital,wght@0,400;0,700;1,400&family=Montserrat:ital,wght@0,400;0,500;1,400&display=swap" rel="stylesheet">
<style>
:root{
  --orange:#ff5a00;
  --amber:#ffa200;
  --ink:#1d1d1d;
  --pale:#eef6fc;
  --white:#ffffff;
  --footer:#000000;
  --muted:#9a9a9a;
  --line:#2a2a2a;
}
*{margin:0;padding:0;box-sizing:border-box}
html,body{width:1200px;height:2861px;overflow:hidden;background:var(--white)}
body{position:relative;font-family:"Montserrat",sans-serif;color:var(--ink)}
.abs{position:absolute}
.serif{font-family:"Playfair Display",serif}

/* hero */
.hero{left:0;top:0;width:1200px;height:696px;overflow:hidden;
  background:linear-gradient(180deg,#e9e9e4 0%,#efe7d2 30%,#f3c98a 55%,#d49a55 70%,#5e4a36 85%,#3a2f25 100%)}
.hero-glow{left:420px;top:260px;width:360px;height:320px;border-radius:50%;
  background:radial-gradient(circle,rgba(255,250,225,.95) 0%,rgba(255,210,120,.5) 45%,rgba(255,200,120,0) 75%)}
.brand{left:111px;top:22px;width:159px;height:158px;border-radius:50%;background:var(--white);
  display:flex;align-items:center;justify-content:center;text-align:center;
  font-family:"Playfair Display",serif;font-size:17px;line-height:1.2;color:var(--orange)}
.topbar{right:113px;top:24px;display:flex;align-items:center;gap:18px}
.phone{display:flex;align-items:center;gap:8px;font-family:"Playfair Display",serif;font-size:21px;color:var(--orange)}
.donate{width:187px;height:38px;background:var(--orange);color:var(--white);font-family:"Playfair Display",serif;
  font-size:21px;display:flex;align-items:center;justify-content:center;letter-spacing:.5px}
.nav{left:301px;top:93px;display:flex;gap:31px;font-family:"Playfair Display",serif;font-size:15px;letter-spacing:.3px;color:#222}
.hero-title{left:0;width:1200px;text-align:center;font-family:"Playfair Display",serif;font-weight:700;
  background:linear-gradient(90deg,var(--orange),var(--amber));-webkit-background-clip:text;background-clip:text;color:transparent;line-height:1}
.t1{top:196px;font-size:226px;letter-spacing:-2px}
.t2{top:368px;left:-20px;font-size:226px;letter-spacing:-2px}
.tabs{left:60px;top:544px;display:flex;gap:14px}
.tab{width:259px;height:52px;background:var(--white);display:flex;align-items:center;justify-content:center;
  font-family:"Playfair Display",serif;font-size:20px;letter-spacing:.5px;color:#1d1d1d;border-radius:3px}
.tab.active{background:var(--orange);color:var(--white)}

/* about */
.about{left:0;top:696px;width:1200px;height:844px;background:var(--pale)}
.about-panel{left:0;top:0;width:576px;height:844px;background:linear-gradient(90deg,var(--orange),var(--amber))}
.founder-photo{left:120px;top:52px;width:486px;height:792px;border-radius:220px 220px 0 0;
  background:linear-gradient(180deg,#c9a48a 0%,#b58b72 25%,#9fc3e4 33%,#1f3a66 45%,#1a2f55 100%)}
.about-head{left:624px;top:92px}
.about-head .small{font-family:"Playfair Display",serif;font-size:44px;line-height:1;color:#1d1d1d}
.about-head .big{font-family:"Playfair Display",serif;font-weight:700;font-size:76px;line-height:1.05;color:var(--orange)}
.rule{height:3px;background:var(--orange)}
.about-rule{left:624px;top:232px;width:237px}
.about-copy{left:623px;top:276px;width:474px;font-size:20px;line-height:31px;color:#222}
.about-copy p+p{margin-top:31px}
.learn{left:623px;top:686px;width:224px;height:59px;border:2px solid var(--orange);background:var(--white);
  display:flex;align-items:center;justify-content:space-between;padding:0 22px 0 24px;
  font-family:"Playfair Display",serif;font-size:18px;color:#222}
.learn .dot{width:42px;height:42px;border-radius:50%;background:var(--orange);display:flex;align-items:center;justify-content:center}

/* testimonials */
.testi-head{left:0;top:1634px;width:1200px;text-align:center}
.testi-head .small{font-family:"Playfair Display",serif;font-size:44px;line-height:1.1;color:#1d1d1d}
.testi-head .big{font-family:"Playfair Display",serif;font-weight:700;font-size:76px;line-height:1;color:var(--orange)}
.testi-rule{left:482px;top:1778px;width:236px}
.card{top:1896px;width:478px;height:375px;background:var(--white);box-shadow:0 6px 22px rgba(0,0,0,.1)}
.card-photo{top:-68px;left:30px;width:206px;height:208px;box-shadow:0 4px 14px rgba(0,0,0,.15)}
.card-meta{left:262px;top:28px}
.quote{font-family:"Playfair Display",serif;font-size:56px;line-height:.6;color:var(--orange);height:30px}
.cname{font-family:"Playfair Display",serif;font-size:23px;font-weight:400;margin-top:6px;color:#111}
.role{font-size:13px;margin-top:6px;color:#222}
.stars{margin-top:8px;display:flex;gap:4px}
.card-rule{left:22px;top:177px;width:434px;height:2px;background:#e3e3e3}
.card-text{left:30px;top:212px;width:418px;text-align:center;font-style:italic;font-size:13.3px;line-height:22px;color:#222}

/* footer */
.footer{left:0;top:2370px;width:1200px;height:491px;background:var(--footer);color:var(--white)}
.fcol-line{top:0;width:1px;height:283px;background:var(--line)}
.seal{left:117px;top:39px;width:204px;height:204px;border-radius:50%;border:3px solid var(--white);
  display:flex;align-items:center;justify-content:center;text-align:center;font-family:"Playfair Display",serif;font-size:19px;line-height:1.25}
.fhead{font-family:"Playfair Display",serif;font-size:15px;letter-spacing:.3px;color:var(--white)}
.fsmall{font-size:13px;line-height:22px;color:#9a9a9a}
.fphone{font-size:27px;color:var(--orange);font-weight:500;letter-spacing:.5px}
.social{display:flex;gap:18px}
.social span{width:25px;height:25px;border:2px solid var(--orange);border-radius:50%}
.email{left:908px;top:113px;width:180px;height:42px;border:1px solid #bdbdbd;border-radius:3px;
  font-size:12px;color:#bbb;display:flex;align-items:center;padding-left:14px}
.subscribe{left:908px;top:163px;width:180px;height:42px;background:var(--orange);border-radius:3px;
  font-family:"Playfair Display",serif;font-size:17px;letter-spacing:2px;display:flex;align-items:center;justify-content:center}
.fline{left:0;width:1200px;height:1px;background:var(--line)}
.fabout{left:120px;top:320px;width:960px;text-align:center;font-size:12.5px;line-height:23px;color:#9a9a9a}
.copy{left:0;top:436px;width:1200px;text-align:center;font-size:12.5px;color:#7a6a55}
</style>
</head>
<body>

<section class="abs hero">
  <div class="abs hero-glow"></div>
  <div class="abs" role="img" aria-label="Photo of two martial artists kicking on a beach at sunset" style="left:0;top:0;width:1200px;height:696px"></div>
  <div class="abs brand">Serene<br>Accord<br>Academy</div>
  <div class="abs topbar">
    <div class="phone">
      <svg width="34" height="34" viewBox="0 0 34 34"><circle cx="17" cy="17" r="16" fill="#ff8a00"/><circle cx="17" cy="17" r="12" fill="#2a6fb5"/><path d="M12.5 10.5l3 3-1.6 1.8c.8 1.7 2.1 3 3.8 3.8l1.8-1.6 3 3-1.8 2c-5.2-.4-9.8-5-10.2-10.2z" fill="#fff"/></svg>
      555-014-2290
    </div>
    <div class="donate">DONATE NOW</div>
  </div>
  <nav class="abs nav">
    <span>SCHOOL FOUNDATIONS</span><span>CURRICULUM</span><span>PEDAGOGY</span><span>OUTCOMES</span><span>OPENING</span><span>TESTIMONIALS</span>
  </nav>
  <div class="abs hero-title t1">MARTIAL</div>
  <div class="abs hero-title t2">ARTS</div>
  <div class="abs tabs">
    <div class="tab">CURRICULAR THEMES</div>
    <div class="tab">CREATIVE EXPRESSION</div>
    <div class="tab active">MARTIAL ARTS</div>
    <div class="tab">SPORTS, &amp; MEDITATIO</div>
  </div>
</section>

<section class="abs about">
  <div class="abs about-panel"></div>
  <div class="abs founder-photo" role="img" aria-label="Portrait of the founder in a navy suit with arms crossed"></div>
  <div class="abs about-head">
    <div class="small">ABOUT</div>
    <div class="big">FOUNDER</div>
  </div>
  <div class="abs rule about-rule"></div>
  <div class="abs about-copy">
    <p>I am creating a K-12 school that is a complete and total re-imagination of what education can be for children, families, com-munities, and the planet. While we will begin as a K-12 school, I really see it as a complete life cycle education (birth to death).</p>
    <p>I am the Founder. I am easy to work with, an effective communicator, and I’m very good at knowing what I want and providing specific and concrete detail, examples, and direction to make sure I use your time wisely.</p>
  </div>
  <div class="abs learn">LEARN MORE
    <span class="dot"><svg width="22" height="16" viewBox="0 0 22 16"><path d="M1 8h18M13 2l6 6-6 6" fill="none" stroke="#fff" stroke-width="2.2"/></svg></span>
  </div>
</section>

<section>
  <div class="abs testi-head">
    <div class="small">Our Happy Clients</div>
    <div class="big">TESTIMONIALS</div>
  </div>
  <div class="abs rule testi-rule"></div>

  <article class="abs card" style="left:111px">
    <div class="abs card-photo" role="img" aria-label="Photo of a smiling family outdoors under a blue sky" style="background:linear-gradient(180deg,#3f8fd8,#8cc3ee 60%,#d9e9f5)"></div>
    <div class="abs card-meta">
      <div class="quote">“</div>
      <div class="cname">Laura M. Bennett</div>
      <div class="role">Podiatric surgeon</div>
      <div class="stars">
        <svg width="94" height="14" viewBox="0 0 94 14" fill="#ff7a00"><g id="s"><path d="M7 0l2 4.6 5 .4-3.8 3.2 1.2 4.8L7 10.4 2.6 13l1.2-4.8L0 5l5-.4z"/></g><use href="#s" x="20"/><use href="#s" x="40"/><use href="#s" x="60"/><use href="#s" x="80"/></svg>
      </div>
    </div>
    <div class="abs card-rule"></div>
    <p class="abs card-text">Sed ut perspiciatis unde omnis iste natus error sit voluptatem accusantium doloremque laudantium, totam rem aperiam, eaque ipsa quae ab illo inventore veritatis et quasi architecto beatae vitae dicta sunt explicabo. Nemo enim ipsam voluptatem quia voluptas sit aspernatur aut odit aut fugit, sed quia consequuntur</p>
  </article>

  <article class="abs card" style="left:612px">
    <div class="abs card-photo" role="img" aria-label="Photo of a family sitting together on a sofa" style="background:linear-gradient(180deg,#e8e8e6,#c7c2bb 50%,#5a6f8e)"></div>
    <div class="abs card-meta">
      <div class="quote">“</div>
      <div class="cname">Nadia K. Harlow</div>
      <div class="role">Recruiting manager</div>
      <div class="stars">
        <svg width="94" height="14" viewBox="0 0 94 14" fill="#ff7a00"><use href="#s"/><use href="#s" x="20"/><use href="#s" x="40"/><use href="#s" x="60"/><use href="#s" x="80"/></svg>
      </div>
    </div>
    <div class="abs card-rule"></div>
    <p class="abs card-text">Sed ut perspiciatis unde omnis iste natus error sit voluptatem accusantium doloremque laudantium, totam rem aperiam, eaque ipsa quae ab illo inventore veritatis et quasi architecto beatae vitae dicta sunt explicabo. Nemo enim ipsam voluptatem quia voluptas sit aspernatur aut odit aut fugit, sed quia consequuntur</p>
  </article>
</section>

<footer class="abs footer">
  <div class="abs fcol-line" style="left:379px"></div>
  <div class="abs fcol-line" style="left:657px"></div>
  <div class="abs fcol-line" style="left:866px"></div>
  <div class="abs seal">Serene<br>Accord<br>Academy</div>

  <div class="abs" style="left:419px;top:60px">
    <div class="fhead">CONTACT INFO</div>
    <div class="fsmall" style="margin-top:12px">248 Maple Crest Lane<br>Fairview, MD 20610</div>
    <div class="fphone" style="margin-top:14px">555-014-2290</div>
    <div class="social" style="margin-top:22px"><span></span><span></span><span></span></div>
  </div>

  <div class="abs" style="left:697px;top:60px">
    <div class="fhead">QUICK LINKS</div>
    <div class="fsmall" style="margin-top:12px">Home<br>School Foundations<br>Curriculum<br>Pedagogy<br>Outcomes<br>Opening<br>Testimonials</div>
  </div>

  <div class="abs fhead" style="left:907px;top:60px">NEWSLETTER SIGN UP</div>
  <div class="abs email">Enter your E - mail</div>
  <div class="abs subscribe">SUBSCRIBE</div>

  <div class="abs fline" style="top:283px"></div>
  <p class="abs fabout">Lorem Ipsum is simply dummy text of the printing and typesetting industry. Lorem Ipsum has been the industry's standard dummy text ever since the 1500s, when an unknown printer took a galley of type and scrambled it to make a type specimen book. It has survived .</p>
  <div class="abs fline" style="top:387px"></div>
  <div class="abs copy">*Copyright Serene Accord Academy 2023 All Rights Reserved</div>
</footer>

</body>
</html>
```